Mobile Recording Studio needs business cards

Open to seeing a creative design, but I want to emphasis my logo and minimize the name/title and company information. Possible a fully black background on card.

My company is a mobile sound recording studio. ok to include a my trailer (actual or cartoon) on the card. My initial thought is more straight forward, but a good design will win me over.

SPECS:
CMYK color mode
High (300ppi) raster effect.
cover bleed area
please deliver: Illustrator file with layers and a pdf at completion.

Name and info for the business card:

Dallin Perry
ADR Mixer

email: Dallin@MixVault.com

address:
248 - 5170 East Hollister
Vancouver, BC V5R 2J4

phone:
604.518.2093 office

website:
www.MixVault.com

FB: @MixVault

Instagram: @TheMixVault

Industry/Entity Type

Television Production

Contact Information for Business Card

Dallin Perry
ADR Mixer

email: Dallin@MixVault.com

address:
248 - 5170 East Hollister
Vancouver, BC V5R 2J4

phone:
604.518.2093 office

website:
www.MixVault.com

FB: @MixVault

Instagram: @TheMixVault

Colors

Designer to choose colors to be used in the design.

Requirements
Must have
• emphasis my logo and minimize the name/title and company information.
• SPECS:
• CMYK color mode
• High (300ppi) raster effect.
• cover bleed area
• please deliver: Illustrator file with layers and a pdf at completion.
Nice to have
• maybe include the following:
• all black background or black theme
• my work trailer (actual or cartoon) refer to Instagram: @TheMixVault

```html
<!DOCTYPE html>
<html lang="en">
<head>
<meta charset="utf-8">
<title>MixVault Business Cards</title>
<link rel="stylesheet" href="https://fonts.googleapis.com/css2?family=Cinzel:wght@600&family=Montserrat:wght@400&display=swap">
<style>
  :root {
    --page: #2a2a2c;
    --card: #050505;
    --silver: #d6d6d8;
    --text: #e9e9ea;
    --muted: #bdbdbf;
    --rule: #8c8c8e;
    --stripe: #f4f4f4;
  }
  * { box-sizing: border-box; margin: 0; padding: 0; }
  html, body { width: 1200px; height: 900px; overflow: hidden; }
  body {
    background: radial-gradient(ellipse at 55% 45%, #3a3a3d 0%, var(--page) 70%);
    font-family: "Montserrat", Arial, sans-serif;
    color: var(--text);
    position: relative;
  }
  .card {
    position: absolute;
    left: 250px;
    width: 700px;
    height: 400px;
    background: var(--card);
    overflow: hidden;
    box-shadow: 0 14px 30px rgba(0,0,0,.55);
  }
  .card--back { top: 35px; }
  .card--front { top: 465px; }

  .trailer-photo {
    position: absolute;
    left: 250px; top: 0; right: 0; bottom: 0;
    background:
      linear-gradient(90deg, var(--card) 0%, rgba(5,5,5,0) 30%),
      linear-gradient(180deg, #2b2d30 0%, #1a1b1d 35%, #101112 60%, #0b0b0c 100%);
  }
  .stripe {
    position: absolute;
    bottom: 22px;
    height: 4px;
    background: var(--stripe);
  }
  .stripe--left { left: 0; width: 380px; }
  .stripe--right { left: 394px; right: 0; }

  .brand {
    font-family: "Cinzel", Georgia, serif;
    font-weight: 600;
    color: var(--silver);
    letter-spacing: 1px;
    line-height: 1;
    white-space: nowrap;
  }
  .card--back .brand { position: absolute; left: 60px; top: 110px; font-size: 66px; }
  .card--front .brand { position: absolute; left: 40px; top: 165px; font-size: 56px; }

  .website {
    position: absolute; left: 60px; top: 235px;
    font-size: 17px; letter-spacing: 5px; color: var(--text);
  }
  .socials {
    position: absolute; right: 40px; bottom: 52px;
    display: flex; gap: 46px; font-size: 17px;
  }
  .social { display: flex; align-items: center; gap: 10px; }
  .social__mark { width: 14px; height: 14px; background: var(--text); }
  .social__mark--round { border-radius: 50%; background: none; border: 2px solid var(--text); }

  .contact {
    position: absolute; left: 385px; top: 80px; width: 300px;
    font-size: 15px; line-height: 1.3; white-space: nowrap;
  }
  .contact__name {
    font-family: "Cinzel", Georgia, serif; font-weight: 600;
    font-size: 15px; color: var(--muted); letter-spacing: .5px;
  }
  .contact__divider { width: 130px; height: 1px; background: var(--rule); margin: 8px 0 10px; }
  .contact__address { margin-top: 22px; font-size: 16px; }
  .contact__phone { margin-top: 16px; display: flex; align-items: center; gap: 12px; font-size: 16px; }
</style>
</head>
<body>
  <section class="card card--back">
    <div class="trailer-photo" role="img" aria-label="Dim dusk photo of the black MixVault recording trailer and truck parked in front of bare trees"></div>
    <div class="brand">MixVault</div>
    <div class="website">www.MixVault.com</div>
    <div class="socials">
      <div class="social"><span class="social__mark"></span>@MixVault</div>
      <div class="social"><span class="social__mark social__mark--round"></span>@TheMixVault</div>
    </div>
    <div class="stripe stripe--left"></div>
    <div class="stripe stripe--right"></div>
  </section>

  <section class="card card--front">
    <div class="brand">MixVault</div>
    <div class="contact">
      <div class="contact__name">Dallin Perry</div>
      <div>ADR Mixer</div>
      <div class="contact__divider"></div>
      <div class="contact__name">Reid Holloway</div>
      <div>Engineer / Director of Operations</div>
      <div class="contact__address">248 - 5170 East Hollister<br>Vancouver, BC V5R 2J4</div>
      <div class="contact__phone">
        <svg width="16" height="14" viewBox="0 0 16 14" aria-hidden="true">
          <path d="M1 4 Q8 -1 15 4 L13 6 L11 4.5 L11 3 Q8 2 5 3 L5 4.5 L3 6 Z" fill="#e9e9ea"/>
          <rect x="3" y="7" width="10" height="6" rx="1" fill="#e9e9ea"/>
        </svg>
        604.518.2093
      </div>
    </div>
    <div class="stripe stripe--left"></div>
    <div class="stripe stripe--right"></div>
  </section>
</body>
</html>
```